New solo practice law firm is looking for an elegant, professional, and interactive web design

I need a web design and developer for a new small law firm in Sacramento, California called Dorian Kessel Law, A Professional Corporation. I am a trial lawyer who represents average people facing difficult litigation disputes, including criminal defense as a former prosecutor and civil litigation as a civil litigator. Criminal defense includes domestic violence, battery, assault, drug possession, theft, DUI, etc. Civil litigation includes business disputes, property disputes, employment disputes, family law disputes, and immigration issues. I would like to see web designs that incorporate my logo and use the logo's navy blue and gold colors. I have uploaded the files of my logo to this brief. Please only use the navy blue and gold version. Overall, I want the design to look firm, professional, and elegant.

I plan on having the following pages on my website: (1) Home, (2) Dorian Kessel, (3) Practice Areas, (4) Insights, (5) Contact. I've hand drawn a preliminary sketch concept of what I envision the home page's layout to look like (attached with a text version). I would like your design to keep a similar layout for the homepage and incorporate my logo's colors within it but I am open to creative layout alternatives/ideas. I would like the other pages to have a similar look and feel as the home page. Some of the areas currently in my sketch do not have the full text. You can insert other text for now and I will provide the winner the full text.

In terms of the pictures on the website, I enjoy images of courthouses, columns (example attached but I cannot use this one), and, if possible, images from Sacramento, CA in my background (headshot attached). A plus would be live images that move and also sections of the webpage moving in the viewers view as they scroll down on the page. Also, it would be great to have my logo act as the tab for the website. I can provide other versions of the logo if needed.

I look forward to seeing your Wordpress designs!

People needing legal representation.

Law

Coded - Design and coding required

5+ page

Serif

• Incorporate my logo and my logo's colors.
• Live pictures and images appearing as viewers scroll on page.

```html
<!DOCTYPE html>
<html lang="en">
<head>
<meta charset="utf-8">
<title>Dorian Kessel Law</title>
<link href="https://fonts.googleapis.com/css2?family=Playfair+Display:wght@400;700&family=Montserrat:wght@400;500;600;700&display=swap" rel="stylesheet">
<style>
:root{
  --navy:#15223a;
  --navy-deep:#0f1a2e;
  --gold:#b4985f;
  --tan:#a8916a;
  --ink:#2a2a2a;
  --muted:#5c5c5c;
  --line:#d7d7d7;
  --white:#ffffff;
}
*{box-sizing:border-box;margin:0;padding:0}
html,body{width:1200px;height:2888px;overflow:hidden}
body{font-family:"Montserrat",sans-serif;color:var(--ink);background:var(--white);position:relative}
a{text-decoration:none}

/* header */
.topbar{position:absolute;left:0;top:0;width:1200px;height:100px;background:var(--navy)}
.brand{position:absolute;left:112px;top:22px;display:flex;align-items:center;gap:12px}
.brand-mark{width:52px;height:52px;border:2px solid var(--gold)}
.brand-name{font-family:"Playfair Display",serif;color:var(--gold);font-size:13px;line-height:1.35;letter-spacing:1px;text-transform:uppercase;width:190px}
.lang{position:absolute;left:608px;top:38px;display:flex;align-items:center;gap:8px;color:var(--white);font-size:13px;font-weight:600}
.lang-flag{width:22px;height:14px;background:#c8102e;border:2px solid #fff;outline:2px solid #1d3a7a}
.address{position:absolute;left:730px;top:24px;display:flex;gap:12px;align-items:center;color:var(--white);font-size:11px;line-height:1.45;font-weight:500;text-transform:uppercase}
.icon-ring{width:40px;height:40px;border:2px solid var(--gold);border-radius:50%;display:flex;align-items:center;justify-content:center;flex:none}
.phone-box{position:absolute;left:980px;top:0;width:220px;height:100px;background:var(--gold);display:flex;align-items:center;gap:12px;padding-left:20px;color:var(--white)}
.phone-box .icon-ring{border-color:var(--white)}
.phone-label{font-size:11px;font-weight:600;text-transform:uppercase;letter-spacing:.5px}
.phone-num{font-size:17px;font-weight:700}
.mainnav{position:absolute;left:0;top:100px;width:1200px;height:32px;background:var(--tan);display:flex;justify-content:center;gap:52px;align-items:center}
.mainnav a{color:var(--white);font-size:12px;font-weight:600;letter-spacing:1.2px;text-transform:uppercase}
.mainnav a.active{border-bottom:2px solid var(--white);padding-bottom:2px}

/* hero */
.hero{position:absolute;left:0;top:132px;width:1200px;height:508px;
  background:
    radial-gradient(ellipse 240px 330px at 150px 330px,rgba(20,24,34,.85),rgba(20,24,34,0) 70%),
    radial-gradient(ellipse 200px 300px at 770px 200px,rgba(186,140,70,.75),rgba(186,140,70,0) 70%),
    linear-gradient(180deg,#9fb8cf 0%,#c9d2d6 38%,#c7a878 58%,#6b6252 78%,#3c4148 100%)}
.hero-arrow{position:absolute;top:230px;width:46px;height:46px;border:2px solid rgba(255,255,255,.9);border-radius:50%;display:flex;align-items:center;justify-content:center}
.hero-arrow.prev{left:34px}
.hero-arrow.next{right:34px}

/* intro */
.intro{position:absolute;left:0;top:690px;width:1200px;text-align:center}
.section-title{font-family:"Playfair Display",serif;font-weight:700;text-transform:uppercase;letter-spacing:3px;font-size:32px;color:var(--navy-deep)}
.intro p{width:540px;margin:18px auto 0;font-size:14px;line-height:1.75;color:var(--muted)}
.practice{position:absolute;left:112px;top:888px;display:flex;gap:16px}
.practice-card{width:232px;height:260px;background:var(--white);box-shadow:0 3px 14px rgba(0,0,0,.14);text-align:center}
.practice-img{height:200px;margin:6px 6px 0}
.practice-card h3{font-family:"Playfair Display",serif;font-weight:400;font-size:14px;letter-spacing:2px;text-transform:uppercase;color:var(--navy-deep);margin-top:20px}

/* about */
.about{position:absolute;left:0;top:1240px;width:1200px;height:480px;background:var(--navy);overflow:hidden}
.about-text{position:absolute;left:112px;top:72px;width:560px;color:var(--white)}
.about-text h2{font-family:"Playfair Display",serif;font-weight:700;font-size:24px;letter-spacing:2px;text-transform:uppercase;white-space:nowrap}
.about-text p{font-size:13px;line-height:1.7;margin-top:22px;color:#e4e7ee;width:520px}
.btn{display:inline-block;background:var(--gold);color:var(--white);font-size:13px;font-weight:700;letter-spacing:2px;text-transform:uppercase;padding:13px 34px}
.about-text .btn{margin-top:30px}
.about-arc{position:absolute;left:800px;top:70px;width:520px;height:520px;border-radius:50%;background:var(--gold)}
.about-photo{position:absolute;left:850px;top:60px;width:230px;height:420px;border-radius:110px 110px 0 0;
  background:radial-gradient(ellipse 70px 90px at 115px 90px,#8a6a52,rgba(138,106,82,0) 75%),linear-gradient(180deg,#3a2e26 0%,#23272f 40%,#141a26 100%)}

/* consultation */
.consult{position:absolute;left:0;top:1836px;width:1200px;text-align:center}
.consult p{width:620px;margin:18px auto 0;font-size:13px;line-height:1.65;color:var(--muted)}
.consult-form{position:absolute;left:340px;top:1990px;width:520px}
.field{height:40px;border:1px solid var(--line);display:flex;align-items:center;padding-left:14px;font-size:12px;color:#8a8a8a;margin-bottom:16px}
.field-row{display:flex;gap:16px}
.field-row .field{flex:1}
.field.message{height:160px;align-items:flex-start;padding-top:12px}
.submit{position:absolute;left:490px;top:2276px;width:220px;text-align:center;padding:13px 0}

/* footer */
.footer{position:absolute;left:0;top:2400px;width:1200px;height:488px;background:var(--navy-deep);color:var(--white)}
.footer-brand{position:absolute;left:120px;top:60px;width:250px;text-align:center}
.footer-brand .brand-mark{width:110px;height:110px;margin:0 auto 16px}
.footer-brand .brand-name{width:auto;font-size:14px}
.footer-col{position:absolute;top:66px}
.footer-col h4{font-size:15px;font-weight:700;letter-spacing:1px;text-transform:uppercase;margin-bottom:18px}
.footer-col li{list-style:none;font-size:12px;line-height:1.9;text-transform:uppercase;font-weight:500}
.col-contact{left:544px}
.col-links{left:860px}
.socials{position:absolute;left:590px;top:250px;display:flex;gap:18px}
.social{width:38px;height:38px;border:2px solid var(--white);border-radius:50%;display:flex;align-items:center;justify-content:center}
.disclaimer{position:absolute;left:160px;top:318px;width:880px;text-align:center;font-size:12px;line-height:1.7;color:#dfe3ea}
.copyright{position:absolute;left:0;top:440px;width:1200px;text-align:center;font-size:12px;color:#dfe3ea}
</style>
</head>
<body>

<header class="topbar">
  <div class="brand">
    <div class="brand-mark"></div>
    <div class="brand-name">Dorian Kessel Law</div>
  </div>
  <div class="lang"><span>ENG</span><span class="lang-flag"></span>
    <svg width="10" height="6" viewBox="0 0 10 6"><path d="M1 1l4 4 4-4" fill="none" stroke="#fff" stroke-width="1.5"/></svg>
  </div>
  <div class="address">
    <span class="icon-ring"><svg width="16" height="20" viewBox="0 0 16 20"><path d="M8 1a6 6 0 0 0-6 6c0 5 6 12 6 12s6-7 6-12a6 6 0 0 0-6-6z" fill="none" stroke="#b4985f" stroke-width="1.8"/><circle cx="8" cy="7" r="2" fill="#b4985f"/></svg></span>
    <span>2150 Capitol Row<br>Suite 410<br>Sacramento, CA 95814</span>
  </div>
  <div class="phone-box">
    <span class="icon-ring"><svg width="18" height="18" viewBox="0 0 24 24"><path d="M6.6 10.8a15 15 0 0 0 6.6 6.6l2.2-2.2a1 1 0 0 1 1-.25 11.4 11.4 0 0 0 3.6.57 1 1 0 0 1 1 1V20a1 1 0 0 1-1 1A17 17 0 0 1 3 4a1 1 0 0 1 1-1h3.5a1 1 0 0 1 1 1c0 1.25.2 2.45.57 3.57a1 1 0 0 1-.25 1z" fill="#fff"/></svg></span>
    <span><span class="phone-label">Free Consultation</span><br><span class="phone-num">(916) 555-0148</span></span>
  </div>
</header>

<nav class="mainnav">
  <a class="active" href="#">Home</a>
  <a href="#">Dorian Kessel</a>
  <a href="#">Practice Areas</a>
  <a href="#">Insights</a>
  <a href="#">Contact</a>
</nav>

<section class="hero" role="img" aria-label="Attorney in a dark suit standing before a golden Sacramento river bridge at dusk">
  <span class="hero-arrow prev"><svg width="16" height="16" viewBox="0 0 16 16"><path d="M10 3L5 8l5 5" fill="none" stroke="#fff" stroke-width="2"/></svg></span>
  <span class="hero-arrow next"><svg width="16" height="16" viewBox="0 0 16 16"><path d="M6 3l5 5-5 5" fill="none" stroke="#fff" stroke-width="2"/></svg></span>
</section>

<section class="intro">
  <h1 class="section-title">Criminal and Civil Trial Lawyers</h1>
  <p>Dorian Kessel Law is a law firm serving the Sacramento, Yolo, San Joaquin, Solano and Stanislaus Counties. We represent clients in a wide array of criminal, civil, family law, and immigration cases.</p>
</section>

<div class="practice">
  <article class="practice-card">
    <div class="practice-img" role="img" aria-label="Hands in handcuffs" style="background:radial-gradient(ellipse 80px 60px at 110px 110px,#b59070,rgba(181,144,112,0) 75%),linear-gradient(160deg,#3e3128,#7a5e48 60%,#a88a6c)"></div>
    <h3>Criminal Defense</h3>
  </article>
  <article class="practice-card">
    <div class="practice-img" role="img" aria-label="Lawyer reviewing documents at a desk" style="background:radial-gradient(ellipse 70px 90px at 120px 90px,#3c4452,rgba(60,68,82,0) 75%),linear-gradient(180deg,#b9b4ab,#d9d1c3 70%,#9a8468)"></div>
    <h3>Civil Litigation</h3>
  </article>
  <article class="practice-card">
    <div class="practice-img" role="img" aria-label="Flags at a border crossing under a blue sky" style="background:linear-gradient(180deg,#4f93d3 0%,#9cc4e4 45%,#d9dde0 62%,#b59f80 100%)"></div>
    <h3>Immigration</h3>
  </article>
  <article class="practice-card">
    <div class="practice-img" role="img" aria-label="Family meeting with an advisor" style="background:radial-gradient(ellipse 90px 70px at 110px 120px,#5a6c86,rgba(90,108,134,0) 75%),linear-gradient(160deg,#c9ccd1,#e4dccf 60%,#a48e74)"></div>
    <h3>Family Law</h3>
  </article>
</div>

<section class="about">
  <div class="about-arc"></div>
  <div class="about-photo" role="img" aria-label="Portrait of the attorney in a dark suit"></div>
  <div class="about-text">
    <h2>Ready, Reliable, and Experienced</h2>
    <p>Our practice was built on a simple promise: every client deserves a lawyer who listens, prepares, and fights. As a former prosecutor and seasoned civil litigator, Dorian brings courtroom experience to each case, from the first consultation to the final verdict, and keeps you informed at every step along the way.</p>
    <p>Whether you face a criminal charge or a civil dispute, we treat your matter with the care it deserves and build a clear strategy toward the best result.</p>
    <a class="btn" href="#">About Dorian</a>
  </div>
</section>

<section class="consult">
  <h2 class="section-title">Schedule a Free Consultation</h2>
  <p>When you contact Dorian Kessel Law — for a free consultation. Tell us briefly about your situation and we will respond within one business day to arrange a confidential meeting.</p>
</section>

<form class="consult-form">
  <div class="field">Full Name</div>
  <div class="field-row">
    <div class="field">Email</div>
    <div class="field">Phone number</div>
  </div>
  <div class="field message">Please write a brief description of your case</div>
</form>
<a class="btn submit" href="#">Submit</a>

<footer class="footer">
  <div class="footer-brand">
    <div class="brand-mark"></div>
    <div class="brand-name">Dorian Kessel Law</div>
  </div>
  <div class="footer-col col-contact">
    <h4>Contact Info</h4>
    <ul><li>2150 Capitol Row</li><li>Suite 410</li><li>Sacramento, CA 95814</li></ul>
  </div>
  <div class="footer-col col-links">
    <h4>Quick Links</h4>
    <ul><li>Home</li><li>Dorian Kessel</li><li>Practice Areas</li><li>Insights</li><li>Contact</li><li>Privacy Policy</li></ul>
  </div>
  <div class="socials">
    <span class="social" aria-label="Email"><svg width="16" height="12" viewBox="0 0 16 12"><rect x="1" y="1" width="14" height="10" fill="none" stroke="#fff" stroke-width="1.5"/><path d="M1 1l7 6 7-6" fill="none" stroke="#fff" stroke-width="1.5"/></svg></span>
    <span class="social" aria-label="Phone"><svg width="15" height="15" viewBox="0 0 24 24"><path d="M6.6 10.8a15 15 0 0 0 6.6 6.6l2.2-2.2a1 1 0 0 1 1-.25 11.4 11.4 0 0 0 3.6.57 1 1 0 0 1 1 1V20a1 1 0 0 1-1 1A17 17 0 0 1 3 4a1 1 0 0 1 1-1h3.5a1 1 0 0 1 1 1c0 1.25.2 2.45.57 3.57a1 1 0 0 1-.25 1z" fill="#fff"/></svg></span>
    <span class="social" aria-label="Location"><svg width="12" height="16" viewBox="0 0 16 20"><path d="M8 1a6 6 0 0 0-6 6c0 5 6 12 6 12s6-7 6-12a6 6 0 0 0-6-6z" fill="none" stroke="#fff" stroke-width="2"/><circle cx="8" cy="7" r="2" fill="#fff"/></svg></span>
  </div>
  <p class="disclaimer">The information on this website is for general information purposes only. Nothing on this site should be taken as legal advice for any individual case or situation. This information is not intended to create, and receipt or viewing does not constitute an attorney-client relationship.</p>
  <p class="copyright">*Copyright 2021 All Rights Reserved</p>
</footer>

</body>
</html>
```